Stellenanzeigen zur Mitarbeitergewinnung über soziale Medien & Google / YouTube
Zielgruppe
Wir sind zwei Brüder und Inhaber der Zahnarztpraxis „ Zahnmedizin im Lindenquartier“ in Bochum.
Wir benötigen zur Mitarbeitergewinnung ein neues, modernes Konzept. Insbesondere stehen Stellenanzeigen im Vordergrund, die in sozialen Medien, wie Instagram, aber auch über Google und YouTube angezeigt werden sollen und potentielle Mitarbeiter auf unsere eigene Landingpage zur Mitarbeitergewinnung führen
Es geht nicht darum, Patienten anzusprechen, sondern ausschließlich um Mitarbeitergewinnung.
Aufgabenstellung
Wir haben Interesse an einem Gesamtkonzept, eine Serie von Anzeigen, die unsere Praxis widerspiegeln, uns als Inhaber zeigen, sowie unsere vorhandenen Mitarbeiterinnen einbinden.
Aufgrund der Vielzahl von Stellenanzeigen im medizinischen Bereich, braucht es neue Ideen. Wir möchten uns deutlich von den vorhandenen, unzähligen Anzeigen bei Instagram abheben. Hier sind kreative Ideen erwünscht.
Wir haben eine zur Mitarbeitergewinnung vorhandene Homepage, die Videos und Aussagekräftige Fotos und Texte beinhaltet. Dort gibt es die Möglichkeit, sich direkt auf eine freie Stelle unkompliziert zu bewerben.
Wir möchten über die neuen Anzeigen potentielle Mitarbeiter dazu bewegen, sich diese Homepage anzusehen und sich gegebenfalls direkt zu bewerben.
Wir freuen uns über ein Gesamtkonzept, gerne verschiedene Stellenanzeigen, die aber ineinander schlüssig sind. Beispielsweise mit anderen Überschriften oder mit verschiedenen Fotos, die wir bereitstellen. Die vorgeschlagenen Fotos können gerne benutzt werden, alternativ sind wir im Hinblick auf das Gesamtkonzept auch offen für andere Ideen und Fotos. Da die Mitbewerbersituation extrem hoch ist, macht es Sinn, sich vorhandene Stellenanzeigen anzusehen, damit wir deutlich die Vorteile unserer Praxis transportieren und uns klar positionieren.
Wir Inhaber, Brüder, Dr. Tobias und Jörg Wessling, sind Ende 30, Ruhrpottkinder, haben eine moderne Praxis zentral in Bochum am Auhof.
Unsere Praxis ist im modernen und ansprechenden Lindenquartier. Wir haben bereits ein großes Team und zwei weitere angestellte Zahnärztinnen. Bei uns gibt es eine faire Bezahlung, Zusatzleistungen, die eine Gutscheinkarte oder die Möglichkeit eines Stellplatzes oder ÖPNV Ticket. Wir machen keine Überstunden, sind freundliche und entspannte Chefs. Wir legen Wert auf Qualität und nehmen uns für uns Zeit für Patienten und Mitarbeiter.
Ziel sollte es sein, motivierte und leistungsstarke Mita..

```html
<!DOCTYPE html>
<html lang="de">
<head>
<meta charset="utf-8">
<title>Stellenanzeige – Zahnmedizin im Lindenquartier</title>
<link rel="stylesheet" href="https://fonts.googleapis.com/css2?family=Poppins:ital,wght@0,400;0,800;1,600&family=Open+Sans:wght@600&display=swap">
<style>
  :root {
    --teal-light: #aef3ea;
    --teal: #6fe8d9;
    --teal-deep: #3fdfce;
    --white: #ffffff;
    --green: #84de2c;
    --gold: #e2b937;
    --ink: #333333;
  }
  html, body {
    margin: 0;
    padding: 0;
    width: 1200px;
    height: 1200px;
    overflow: hidden;
  }
  .ad {
    position: relative;
    width: 1200px;
    height: 1200px;
    overflow: hidden;
    background: radial-gradient(circle at 50% 38%, var(--teal-light) 0%, var(--teal) 45%, var(--teal-deep) 100%);
    font-family: "Poppins", sans-serif;
  }
  .portrait {
    position: absolute;
    left: 240px;
    top: 96px;
    width: 690px;
    height: 900px;
    border-radius: 300px 300px 0 0;
    background: linear-gradient(to bottom, rgba(31,58,54,0.55) 0%, rgba(31,58,54,0.85) 55%, rgba(31,58,54,0.15) 100%);
  }
  .bubble-frame {
    position: absolute;
    inset: 0;
  }
  .brand-card {
    position: absolute;
    left: 70px;
    top: 0;
    width: 260px;
    height: 238px;
    background: var(--white);
    border-radius: 0 0 16px 16px;
    display: flex;
    align-items: center;
    justify-content: center;
  }
  .brand-name {
    margin: 0;
    font-family: "Poppins", sans-serif;
    font-weight: 400;
    font-size: 24px;
    line-height: 1.2;
    color: var(--ink);
    text-align: center;
  }
  .hashtag {
    position: absolute;
    left: 884px;
    top: 52px;
    display: flex;
    gap: 10px;
    font-style: italic;
    font-weight: 600;
    color: var(--white);
    text-shadow: 0 2px 8px rgba(0,0,0,0.12);
  }
  .hashtag-mark {
    font-size: 96px;
    line-height: 0.9;
  }
  .hashtag-words {
    font-size: 46px;
    line-height: 1.05;
  }
  .hashtag-words .accent { color: var(--green); }
  .headline {
    position: absolute;
    left: 0;
    width: 1176px;
    top: 560px;
    margin: 0;
    text-align: center;
    font-weight: 800;
    font-size: 74px;
    line-height: 88px;
    letter-spacing: -1px;
    text-transform: uppercase;
    color: var(--white);
    text-shadow: 0 3px 12px rgba(0,0,0,0.2);
  }
  .headline .accent { color: var(--green); }
  .cta-band {
    position: absolute;
    left: 0;
    top: 1060px;
    width: 1200px;
    height: 140px;
  }
  .cta-label {
    position: absolute;
    left: 0;
    width: 1156px;
    top: 1108px;
    text-align: center;
    font-family: "Open Sans", sans-serif;
    font-weight: 600;
    font-size: 44px;
    color: var(--white);
  }
</style>
</head>
<body>
  <main class="ad">
    <div class="portrait" role="img" aria-label="Porträtfoto einer lächelnden Mitarbeiterin mit langen dunklen Haaren in dunkler Bluse"></div>

    <svg class="bubble-frame" width="1200" height="1200" viewBox="0 0 1200 1200" aria-hidden="true">
      <path d="M0 326 L445 308 M765 296 L1030 288 Q1062 288 1063 320 L1080 930 Q1081 958 1060 962 L962 1048 L998 972 L170 1000 Q125 1001 124 956 L105 445"
            fill="none" stroke="#ffffff" stroke-width="3" stroke-linejoin="round" stroke-linecap="round"/>
    </svg>

    <div class="brand-card">
      <p class="brand-name">Zahnmedizin<br>im Lindenquartier</p>
    </div>

    <div class="hashtag">
      <span class="hashtag-mark">#</span>
      <span class="hashtag-words">BEWIRB<br><span class="accent">DICH</span><br>JETZT!</span>
    </div>

    <h1 class="headline">
      Deine Expertise<br>
      verdient Applaus –<br>
      <span class="accent">Werde Teil unseres<br>Elite-Teams</span>
    </h1>

    <svg class="cta-band" width="1200" height="140" viewBox="0 0 1200 140" aria-hidden="true">
      <path d="M0 44 L1110 8 Q1180 6 1200 60 L1200 140 L0 140 Z" fill="#e2b937"/>
    </svg>
    <div class="cta-label">JETZT MEHR ERFAHREN!</div>
  </main>
</body>
</html>
```